Word document advertising our end of the year specials

We want to post something on our Facebook page and send in an email announcing our winter specials on our golf programs to our current customers. We are offering them a $500 discount if they sign up before the new year $2,000 instead of $2,500. Also, we are offering a referral program, if a current player refers a new client, and that client purchases a practice membership, they will receive $75. If their referral purchases a coaching program, they will receive $150. Lastly, we are hosting an open house on December 1st 11:00-1:00pm for current players and their family and friends**Tee it up for next season now with our winter specials **Reserve your spot now and sign up !
Target Market(s)
Golfers

```html
<!DOCTYPE html>
<html lang="en">
<head>
<meta charset="utf-8">
<title>Winter Specials – Fairway Point Golf</title>
<link rel="stylesheet" href="https://fonts.googleapis.com/css2?family=Exo+2:wght@400;700&family=Open+Sans:wght@600;700&family=Jura:wght@500;700&display=swap">
<style>
  :root {
    --red: #e3101b;
    --ink: #151515;
    --page: #ececec;
    --paper-top: #d9d7d1;
    --paper-mid: #cfcdc5;
    --paper-low: #b9bba9;
    --white: #ffffff;
  }
  * { margin: 0; padding: 0; box-sizing: border-box; }
  html, body { width: 1200px; height: 1200px; overflow: hidden; background: var(--page); }
  .poster {
    position: absolute; left: 206px; top: 20px; width: 788px; height: 1160px;
    overflow: hidden; font-family: "Exo 2", sans-serif; color: var(--red);
  }
  .backdrop {
    position: absolute; inset: 0;
    background:
      radial-gradient(ellipse 190px 240px at 95px 720px, rgba(255,255,255,.95) 0%, rgba(240,240,240,.85) 60%, rgba(255,255,255,0) 100%),
      linear-gradient(180deg, var(--paper-top) 0%, var(--paper-mid) 50%, var(--paper-low) 80%, #c9c9bd 100%);
  }
  .frame {
    position: absolute; left: 14px; top: 16px; right: 14px; bottom: 22px;
    border: 2px solid var(--red); border-radius: 12px;
  }
  .abs { position: absolute; }
  .brand-name {
    left: 43px; top: 224px; width: 300px; text-align: center; white-space: nowrap;
    font-size: 28px; font-weight: 700; line-height: 1;
  }
  .headline {
    left: 300px; top: 88px; width: 428px; text-align: center; white-space: nowrap;
    font-size: 31px; font-weight: 700; line-height: 52px; text-transform: uppercase;
  }
  .reserve {
    left: 120px; top: 313px; width: 554px; height: 117px; text-align: center;
    background: linear-gradient(90deg, rgba(255,255,255,0) 0%, #fff 10%, #fff 90%, rgba(255,255,255,0) 100%);
    font-size: 30px; line-height: 46px; padding-top: 12px; text-transform: uppercase;
  }
  .stamp { left: 118px; top: 496px; width: 96px; height: 96px; }
  .offer-title { left: 229px; top: 505px; font-size: 27px; text-transform: uppercase; white-space: nowrap; }
  .offer-price {
    left: 216px; top: 540px; width: 475px; text-align: center; white-space: nowrap;
    font-family: "Open Sans", sans-serif; font-weight: 600; font-size: 29px; color: var(--ink);
  }
  .offer-price strong { color: var(--red); font-weight: 700; }
  .divider { left: 115px; top: 629px; width: 573px; height: 2px; background: var(--red); }
  .referral-title { left: 256px; top: 671px; font-size: 27px; font-weight: 400; text-transform: uppercase; }
  .reward {
    width: 140px; left: 120px; text-align: center;
    font-family: "Open Sans", sans-serif; font-weight: 700; color: var(--ink); line-height: 1;
  }
  .reward .label { font-size: 18px; }
  .reward .amount { font-size: 27px; color: var(--red); margin: 10px 0 6px; }
  .reward .note { font-size: 14px; }
  .reward-one { top: 737px; }
  .reward-two { top: 833px; }
  .reward-text {
    left: 253px; width: 440px; font-family: "Open Sans", sans-serif; font-weight: 600;
    font-size: 18.5px; line-height: 24px; color: var(--ink);
  }
  .reward-text-one { top: 750px; }
  .reward-text-two { top: 860px; }
  .open-house {
    left: 99px; top: 963px; width: 603px; height: 120px; text-align: center;
    border: 2px solid var(--red); border-radius: 16px; background: rgba(255,255,255,.55);
    font-family: "Jura", sans-serif; font-weight: 500; font-size: 23px; line-height: 32px;
    color: var(--ink); padding-top: 10px; white-space: nowrap;
  }
  .open-house .date { color: var(--red); font-family: "Exo 2", sans-serif; font-weight: 700; font-size: 25px; }
</style>
</head>
<body>
  <main class="poster">
    <div class="backdrop" role="img" aria-label="Soft-focus photo of a white golf ball resting on frosted grass"></div>
    <div class="frame"></div>

    <div class="abs brand-name">Fairway Point Golf</div>

    <h1 class="abs headline">Tee it up for next<br>season now with our<br>winter specials</h1>

    <p class="abs reserve">Reserve your spot now and<br>sign up !</p>

    <svg class="abs stamp" viewBox="0 0 96 96" role="img" aria-label="Discount badge">
      <circle cx="48" cy="48" r="44" fill="rgba(255,255,255,.8)" stroke="#e3101b" stroke-width="2"/>
    </svg>

    <p class="abs offer-title">Sign up before the new year</p>
    <p class="abs offer-price">Pay <strong>$2,000</strong> instead of $2,500</p>

    <div class="abs divider"></div>

    <h2 class="abs referral-title">Referral program</h2>

    <div class="abs reward reward-one">
      <div class="label">Receive</div>
      <div class="amount">$75</div>
      <div class="note">in club credit</div>
    </div>
    <p class="abs reward-text reward-text-one">Refers a new client, and that client purchases<br>a practice membership</p>

    <div class="abs reward reward-two">
      <div class="label">Receive</div>
      <div class="amount">$150</div>
      <div class="note">in club credit</div>
    </div>
    <p class="abs reward-text reward-text-two">Referral purchases a coaching program</p>

    <div class="abs open-house">
      <div>We are hosting an open house on</div>
      <div class="date">December 1st 11:00-1:00pm</div>
      <div>for current players and their family and friends</div>
    </div>
  </main>
</body>
</html>
```